" é uma corretora de seguros, onde trabalharei com todos os ramos: seguro de automovel, vida, seguro viagem, residencia, condominio, transportes, carga... previdencia e tambem com consorcio. "

```html
<!DOCTYPE html>
<html lang="pt-BR">
<head>
<meta charset="utf-8">
<title>RT Corretora de Seguros — Cartão de visita</title>
<link rel="stylesheet" href="https://fonts.googleapis.com/css2?family=Open+Sans:wght@400;600;700&display=swap">
<style>
  :root {
    --page-bg: #ecebe8;
    --card-white: #ffffff;
    --brand-blue: #1676b0;
    --brand-blue-light: #2a8fcc;
    --brand-blue-dark: #0d5a8e;
    --text-white: #ffffff;
    --shadow: rgba(20, 40, 60, 0.22);
  }
  * { margin: 0; padding: 0; box-sizing: border-box; }
  html, body {
    width: 1200px;
    height: 1200px;
    overflow: hidden;
    background: var(--page-bg);
    font-family: "Open Sans", Arial, sans-serif;
  }
  .sheet {
    width: 1200px;
    height: 1200px;
    display: flex;
    flex-direction: column;
    align-items: center;
    justify-content: center;
    gap: 64px;
  }
  .card {
    position: relative;
    width: 880px;
    height: 488px;
    border-radius: 28px;
    box-shadow: 0 14px 34px var(--shadow);
    overflow: hidden;
  }

  /* Front */
  .card-front {
    background: var(--card-white);
    display: flex;
    align-items: center;
    justify-content: center;
  }
  .brand {
    display: flex;
    align-items: center;
    gap: 22px;
  }
  .brand-mark {
    width: 128px;
    height: 128px;
    border-radius: 18px;
    background: var(--brand-blue);
  }
  .brand-name {
    font-weight: 600;
    font-size: 46px;
    color: var(--brand-blue);
    letter-spacing: 0.5px;
  }

  /* Back */
  .card-back {
    background: linear-gradient(135deg, var(--brand-blue-light) 0%, var(--brand-blue) 45%, var(--brand-blue-dark) 100%);
    color: var(--text-white);
    padding: 56px 64px;
  }
  .holder-name {
    font-weight: 700;
    font-size: 40px;
    letter-spacing: 0.3px;
  }
  .card-back .brand {
    position: absolute;
    top: 58px;
    right: 60px;
    gap: 14px;
  }
  .card-back .brand-mark {
    width: 62px;
    height: 62px;
    border-radius: 9px;
    background: var(--card-white);
  }
  .card-back .brand-name {
    font-size: 24px;
    color: var(--text-white);
  }
  .contact-list {
    list-style: none;
    margin-top: 48px;
    display: flex;
    flex-direction: column;
    gap: 16px;
  }
  .contact-item {
    display: flex;
    align-items: center;
    gap: 18px;
    font-weight: 600;
    font-size: 25px;
  }
  .contact-icon {
    width: 26px;
    height: 26px;
    flex: none;
  }
  .address {
    position: absolute;
    left: 64px;
    bottom: 56px;
    font-weight: 600;
    font-size: 24px;
    line-height: 1.45;
  }
</style>
</head>
<body>
  <main class="sheet">
    <section class="card card-front">
      <div class="brand">
        <div class="brand-mark"></div>
        <span class="brand-name">RT Corretora de Seguros</span>
      </div>
    </section>

    <section class="card card-back">
      <h1 class="holder-name">Helena Prado</h1>
      <div class="brand">
        <div class="brand-mark"></div>
        <span class="brand-name">RT Corretora de Seguros</span>
      </div>

      <ul class="contact-list">
        <li class="contact-item">
          <svg class="contact-icon" viewBox="0 0 26 26" aria-hidden="true">
            <circle cx="13" cy="13" r="13" fill="#fff"/>
            <path d="M9 7.5 l2.3 -0.3 1.2 3 -1.5 1 c0.7 1.5 1.8 2.6 3.3 3.3 l1 -1.5 3 1.2 -0.3 2.3 c-0.2 0.8 -1 1.3 -1.8 1.2 C11.5 17.3 8.7 14.5 7.8 9.3 7.7 8.5 8.2 7.7 9 7.5 z" fill="#1676b0"/>
          </svg>
          <span>11 97777.6666</span>
        </li>
        <li class="contact-item">
          <svg class="contact-icon" viewBox="0 0 26 26" aria-hidden="true">
            <circle cx="13" cy="13" r="13" fill="#fff"/>
            <circle cx="13" cy="13" r="3" fill="none" stroke="#1676b0" stroke-width="2"/>
            <path d="M16 13 v1.5 a2 2 0 0 0 4 0 V13 a7 7 0 1 0 -3 5.7" fill="none" stroke="#1676b0" stroke-width="2" stroke-linecap="round"/>
          </svg>
          <span>helena@rtcorretora.com.br</span>
        </li>
        <li class="contact-item">
          <svg class="contact-icon" viewBox="0 0 26 26" aria-hidden="true">
            <circle cx="13" cy="13" r="13" fill="#fff"/>
            <circle cx="13" cy="13" r="7" fill="none" stroke="#1676b0" stroke-width="1.8"/>
            <ellipse cx="13" cy="13" rx="3" ry="7" fill="none" stroke="#1676b0" stroke-width="1.6"/>
            <line x1="6" y1="13" x2="20" y2="13" stroke="#1676b0" stroke-width="1.6"/>
          </svg>
          <span>www.rtcorretora.com.br</span>
        </li>
      </ul>

      <address class="address">
        Rua das Acácias, 120 Centro - São Paulo / SP<br>
        Tel. 11 3210.5678
      </address>
    </section>
  </main>
</body>
</html>
```